Visitenkarten-Design für Immobilienfinanzierer
Zielgruppe
Ich bin hauptsächlich Immobilienfinanzierer. Das bedeutet, dass ich als unabhängiger Finanzmakler für meine Kunden aus über 400 Banken, Versicherungsgesellschaften und Bausparkassen den Finanzierungspartner auswähle, der die beste Kondition anbietet, oder das Projekt überhaupt begleitet. Die durch die Baufinanzierung gewonnenen Kunden berate ich auch zu den Themen Bausparen, Versicherungen, Vermögensanlagen und Privatkredite. Kernthema mit 80% Umsatzanteil ist die Bau/Immobilienfinanzierung. Mitbewerber mit ähnlichem Geschäftsmodell sind hauptsächlich Dr. Wendau, Baveron.
Aufgabenstellung
In meiner Branche ist Seriosität das Maß aller Dinge. Dabei möchte ich eher modern als altbacken auftreten (kein 'Kanzlei'-Design', aber auch nicht zu flippig. Ich bin 40 Jahre alt, und möchte auch mit 60 noch zum Design passen.

```html
<!DOCTYPE html>
<html lang="de">
<head>
<meta charset="utf-8">
<title>Visitenkarte Velora Private Finance</title>
<link href="https://fonts.googleapis.com/css2?family=Montserrat:wght@600&family=Quicksand:wght@400;500&display=swap" rel="stylesheet">
<style>
  :root {
    --green: #8cb63c;
    --ink: #3b3734;
    --muted: #77726e;
    --rule: #c9c7c4;
    --card: #f6f6f4;
    --stage: #e4e2df;
  }
  * { box-sizing: border-box; margin: 0; padding: 0; }
  html, body { width: 1200px; height: 842px; overflow: hidden; }
  body {
    background: var(--stage);
    font-family: "Quicksand", sans-serif;
    color: var(--ink);
    display: flex;
    align-items: center;
    justify-content: center;
    gap: 40px;
  }
  .card {
    width: 540px;
    height: 348px;
    background: var(--card);
    box-shadow: 0 6px 18px rgba(0,0,0,0.12);
    position: relative;
  }
  /* front side */
  .card-front { display: flex; padding: 44px 0 44px 40px; }
  .contact {
    width: 290px;
    padding-right: 24px;
    border-right: 1.5px solid var(--rule);
    display: flex;
    flex-direction: column;
  }
  .person-name {
    font-family: "Montserrat", sans-serif;
    font-weight: 600;
    font-size: 19px;
    line-height: 1.1;
  }
  .person-role {
    font-family: "Montserrat", sans-serif;
    font-weight: 600;
    font-size: 10.5px;
    color: var(--green);
    letter-spacing: 0.04em;
  }
  .address { margin-top: 26px; font-size: 15px; line-height: 1.15; color: var(--muted); }
  .contact-list { margin-top: auto; font-size: 14.5px; line-height: 1.45; }
  .contact-list .heading { color: var(--muted); }
  .contact-row { display: flex; }
  .contact-row dt { width: 74px; color: var(--green); }
  .contact-row dd { color: var(--ink); }
  .brand-area { flex: 1; display: flex; align-items: center; justify-content: center; }
  .brand {
    display: flex;
    align-items: center;
    gap: 12px;
  }
  .brand-dot { width: 34px; height: 34px; border-radius: 50%; background: var(--green); }
  .brand-name {
    font-family: "Quicksand", sans-serif;
    font-weight: 500;
    font-size: 30px;
    line-height: 1.05;
    color: var(--ink);
  }
  /* back side */
  .card-back { display: flex; align-items: center; justify-content: center; }
  .card-back .brand-dot { width: 70px; height: 70px; }
  .card-back .brand-name { font-size: 48px; }
</style>
</head>
<body>
  <section class="card card-front">
    <div class="contact">
      <p class="person-name">Marlene Hofbauer</p>
      <p class="person-role">IMMOBILIENFINANZIERER</p>
      <p class="address">Lindenweg 7<br>96123 Talbach - OT Hohenried</p>
      <dl class="contact-list">
        <p class="heading">Kontakt</p>
        <div class="contact-row"><dt>Telefon:</dt><dd>00000 / 318 552 4</dd></div>
        <div class="contact-row"><dt>Telefax:</dt><dd>00000 / 318 552 3</dd></div>
        <div class="contact-row"><dt>E-Mail:</dt><dd>info@veloraprivate.de</dd></div>
        <div class="contact-row"><dt>Web:</dt><dd>www.veloraprivate.de</dd></div>
      </dl>
    </div>
    <div class="brand-area">
      <div class="brand">
        <span class="brand-dot"></span>
        <span class="brand-name">Velora<br>Private Finance</span>
      </div>
    </div>
  </section>

  <section class="card card-back">
    <div class="brand">
      <span class="brand-dot"></span>
      <span class="brand-name">Velora</span>
    </div>
  </section>
</body>
</html>
```